VELMAR, an e-commerce website with a twist, providing consumer-to-consumer and business-to-consumer sa

I have only uploaded 10 wire-frame pages of the website. These pages have been chosen for the different lay-outs and should give an idea of what will be needed. There are many more that I won’t upload yet, I aim to choose a winner first then there will be a high possibility that the winner will get the chance to do the design work for these later.
The design I have in mind is to keep it clean and easy with no/minimal fancy fonts and hieroglyphics. The logo is white with an orange highlight on a solid background of black, please note that the logo is white on a black background and is not a black box with white lettering, trust that makes sense. I like the idea of the top part of the website being black all the way across. I don’t see the need for more than 3 colours in the actual base website (the pictures and adverts added by users will add other colours). Although orange is the highlight colour in the logo I am open to suggestions on this, so long as the highlight colour features throughout the site.

Website width is 1220px, all pages in the PDF are 1220px

Logo font is Rezlong

The company is going to be like tradu, but much more focused on raising money for charity and humanitarian relief.

Target Market(s)

the modern era of smartphones and the sharing community

Industry/Entity Type

Business

Number of Pages Required

5+ page

Font styles to use
Sans Serif
Other font styles liked:
• rezlong

Colors
faa54b
f78f20
ffffff
000000
fbfbfb
f5f5f5

Requirements
Nice to have
• Although orange is the highlight colour in the logo I am open to suggestions on this, so long as the highlight colour features throughout the site.

```html
<!DOCTYPE html>
<html lang="en">
<head>
<meta charset="utf-8">
<title>VELMAR – Home</title>
<link rel="stylesheet" href="https://fonts.googleapis.com/css2?family=Roboto:wght@400;500;700&family=Fjalla+One&display=swap">
<style>
:root{
  --orange:#f78f20;
  --orange-light:#faa54b;
  --black:#000000;
  --bar:#1b1c1d;
  --head-top:#2e3133;
  --head-bottom:#1d1f20;
  --white:#ffffff;
  --page:#fbfbfb;
  --muted:#c9c9c9;
  --stage:#e4e4e4;
  --label:rgba(40,42,44,.92);
}
*{box-sizing:border-box;margin:0;padding:0}
html,body{width:1200px;height:900px;overflow:hidden}
body{background:var(--stage);font-family:"Roboto",sans-serif;color:var(--white)}
.site{position:absolute;left:0;top:74px;width:1200px;height:751px;background:var(--page)}
.utility-bar{height:35px;background:var(--bar);display:flex;align-items:center;padding:0 24px;font-size:12.5px;color:var(--muted)}
.utility-bar a{color:var(--muted);text-decoration:none;padding:0 24px;border-right:1px solid #3d3f41;display:flex;align-items:center;gap:6px;line-height:14px}
.utility-bar a:first-child{padding-left:0}
.utility-bar .spacer{flex:1}
.utility-bar .count{color:var(--orange)}
.utility-bar .current{color:var(--white);font-weight:500}
.masthead{height:84px;background:linear-gradient(var(--head-top),var(--head-bottom));display:flex;align-items:center;padding:0 24px}
.brand{font-weight:700;font-size:30px;letter-spacing:-.5px;color:var(--white);margin-right:26px}
.btn{font-size:12.5px;font-weight:700;padding:6px 15px;margin-right:24px;border:1px solid var(--orange)}
.btn-fill{background:var(--orange);color:var(--white)}
.btn-line{color:var(--orange)}
.masthead .spacer{flex:1}
.account{display:flex;align-items:center;gap:10px;font-size:13px;font-weight:500;margin-right:24px}
.icon-box{width:28px;height:26px;border:1px solid #6a6d70;display:flex;align-items:center;justify-content:center;margin-left:24px}
.content{position:relative;height:548px}
.photo{position:absolute;overflow:hidden;box-shadow:0 2px 4px rgba(0,0,0,.3)}
.banner-title{position:absolute;inset:0;display:flex;align-items:center;justify-content:center;font-family:"Fjalla One",sans-serif;color:var(--orange);text-shadow:0 2px 4px rgba(0,0,0,.5)}
.top-banner{left:24px;top:6px;width:1152px;height:98px;background:linear-gradient(90deg,#5a3a2a,#a85a2c 30%,#7a4a30 55%,#c46a34 80%,#b86038)}
.top-banner .banner-title{font-size:56px}
.side-banner{left:590px;width:576px;height:160px}
.side-banner .banner-title{font-size:56px}
.banner-plane{top:154px;background:linear-gradient(#6a6a6a,#585858 60%,#4d4b48)}
.banner-lion{top:339px;background:linear-gradient(90deg,#6e6a62,#5c5a56 45%,#555)}
.tile{width:119px;height:100px}
.tile .label{position:absolute;left:0;right:0;bottom:0;height:22px;background:var(--label);font-size:12.5px;font-weight:700;display:flex;align-items:center;justify-content:center}
.tile-hover .overlay{position:absolute;left:0;right:0;top:36px;height:48px;background:var(--label);display:flex;flex-direction:column;align-items:center;justify-content:center;gap:5px;font-size:12.5px}
.tile-hover .overlay b{font-weight:700}
.tile-hover .overlay span{font-weight:400;color:var(--muted)}
.tile-feature{background:var(--black);display:flex;flex-direction:column;align-items:center;justify-content:center;font-size:14px;font-weight:700;gap:2px}
.tile-feature .brand{margin:0;font-size:28px;line-height:32px}
.footer{height:84px;background:linear-gradient(var(--head-bottom),var(--bar));display:flex;align-items:center;padding:0 24px}
.footer .brand{margin-right:26px}
.footer small{font-size:12.5px;color:var(--muted);margin-top:8px}
.footer .spacer{flex:1}
.social{display:flex;gap:18px;font-size:12.5px;font-weight:500;color:var(--white)}
</style>
</head>
<body>
<div class="site">
  <nav class="utility-bar">
    <a href="#"><svg width="12" height="12" viewBox="0 0 12 12" fill="none" stroke="#f78f20" stroke-width="1.2"><rect x="1" y="2" width="9" height="9"/><path d="M5 7l6-6"/></svg>Notifications <span class="count">(0)</span></a>
    <a href="#">News</a>
    <a href="#" style="border:0">List Item</a>
    <span class="spacer"></span>
    <a href="#">Contact Us</a>
    <a href="#" class="current">Help</a>
    <a href="#">Terms and Conditions</a>
    <a href="#"><svg width="12" height="12" viewBox="0 0 12 12" fill="none" stroke="#c9c9c9" stroke-width="1.3"><circle cx="5" cy="5" r="3.8"/><path d="M8 8l3 3"/></svg>Search</a>
  </nav>

  <header class="masthead">
    <span class="brand">VELMAR</span>
    <span class="btn btn-fill">SIGN UP</span>
    <span class="btn btn-line">SIGN IN</span>
    <span class="spacer"></span>
    <span class="account"><svg width="14" height="12" viewBox="0 0 14 12" fill="none" stroke="#fff" stroke-width="1.3"><circle cx="7" cy="4" r="3"/><path d="M1 11.5h12"/></svg>My Account</span>
    <span class="icon-box"><svg width="14" height="13" viewBox="0 0 14 13" fill="none" stroke="#fff" stroke-width="1.2"><path d="M7 12L1.6 6.4A3.2 3.2 0 0 1 7 2.2a3.2 3.2 0 0 1 5.4 4.2z"/></svg></span>
    <span class="icon-box"><svg width="12" height="14" viewBox="0 0 12 14" fill="none" stroke="#fff" stroke-width="1.2"><rect x="1" y="5" width="10" height="8"/><path d="M3.5 5V3.5a2.5 2.5 0 0 1 5 0V5"/></svg></span>
  </header>

  <main class="content">
    <div class="photo top-banner" role="img" aria-label="Advert photo of red rock canyon landscape"><span class="banner-title">Nice Advert Banner</span></div>

    <div class="photo tile" style="left:24px;top:154px;background:linear-gradient(90deg,#3a2418,#7a4a2a,#a0683c)" role="img" aria-label="Charity photo of an old window interior"><span class="label">Charity Name</span></div>
    <div class="photo tile" style="left:167px;top:154px;background:linear-gradient(135deg,#d8c8b4,#9a8c80 60%,#5a5a5c)" role="img" aria-label="Charity photo of phones on a table"><span class="label">Charity Name</span></div>
    <div class="photo tile tile-hover" style="left:310px;top:147px;background:linear-gradient(#d8e0e6,#8f9aa2 60%,#4f5358)" role="img" aria-label="Charity photo of a city skyline"><div class="overlay"><b>Charity Name</b><span>Charity Detail</span></div></div>
    <div class="photo tile" style="left:452px;top:154px;background:linear-gradient(135deg,#e8e4dc,#8a8078 50%,#4a4440)" role="img" aria-label="Charity photo of a curved sculpture"><span class="label">Charity Name</span></div>

    <div class="photo tile" style="left:24px;top:277px;background:linear-gradient(90deg,#6a5a4e,#b8a898 60%,#d6c8b8)" role="img" aria-label="Charity photo of a wooden house"><span class="label">Charity Name</span></div>
    <div class="photo tile tile-feature" style="left:167px;top:277px"><span>Charities</span><span class="brand">VELMAR</span><span>Supported</span></div>
    <div class="photo tile" style="left:310px;top:277px;background:linear-gradient(135deg,#5a4a40,#8a6a54 50%,#3a3430)" role="img" aria-label="Charity photo of a barista making coffee"><span class="label">Charity Name</span></div>
    <div class="photo tile" style="left:452px;top:277px;background:linear-gradient(135deg,#3a2a1c,#b8782a 50%,#e8c088)" role="img" aria-label="Charity photo of a drink being poured"><span class="label">Charity Name</span></div>

    <div class="photo tile" style="left:24px;top:400px;background:linear-gradient(#2a6a8a,#58a0b8 55%,#d8e4e8)" role="img" aria-label="Charity photo of clouds in a blue sky"><span class="label">Charity Name</span></div>
    <div class="photo tile" style="left:167px;top:400px;background:linear-gradient(135deg,#3a2a18,#5a4028 70%,#c8b898)" role="img" aria-label="Charity photo of a crescent moon"><span class="label">Charity Name</span></div>
    <div class="photo tile" style="left:310px;top:400px;background:linear-gradient(#e8ecec,#c8ccc0 60%,#6a7a50)" role="img" aria-label="Charity photo of palm trees"><span class="label">Charity Name</span></div>
    <div class="photo tile" style="left:452px;top:400px;background:linear-gradient(#7a9ab8,#c8d4dc 60%,#8a9a9a)" role="img" aria-label="Charity photo of a calm sky over land"><span class="label">Charity Name</span></div>

    <div class="photo side-banner banner-plane" role="img" aria-label="Advert photo of vintage aircraft on an airfield"><span class="banner-title">Nice Advert Banner</span></div>
    <div class="photo side-banner banner-lion" role="img" aria-label="Advert photo of a lion"><span class="banner-title">Nice Advert Banner</span></div>
  </main>

  <footer class="footer">
    <span class="brand">VELMAR</span>
    <small>All Rights Reserved.</small>
    <span class="spacer"></span>
    <span class="social"><span>Pinly</span><span>Linkwork</span><span>Viewtube</span><span>Snapgram</span><span>Circleplus</span><span>Facenet</span><span>Chirper</span></span>
  </footer>
</div>
</body>
</html>
```